Commercial Office Fitout company needs a simple website

We need a website for our company Tallow Bridge (QLD) Pty Ltd. We are in the construction industry and we specialise in commercial office fitouts (partitions/glass/doors). Our company colours are black and silver. Please use our logo attached.
We only need an "about us" section, a "portfolio" section where we display some pictures of our work, and a "contact us" section. We would like our website to be simple, effective, professional and modern.

Industry/Entity Type

Construction

Number of Pages Required

1 page

```html
<!DOCTYPE html>
<html lang="en">
<head>
<meta charset="utf-8">
<title>Tallow Bridge (QLD) Pty Ltd — Commercial Office Fit Outs</title>
<link rel="stylesheet" href="https://fonts.googleapis.com/css2?family=Russo+One&family=Oswald:wght@400&family=Lato:wght@400;700&display=swap">
<style>
:root{
  --ink:#1b1b1b;
  --charcoal:#2a2a2a;
  --steel:#8d8f91;
  --silver:#c9cacb;
  --mist:#f4f4f4;
  --white:#ffffff;
  --night:#1c1d1f;
  --footer:#121212;
}
*{box-sizing:border-box;margin:0;padding:0}
html,body{width:668px;height:1200px;overflow:hidden;background:var(--white)}
body{position:relative;font-family:"Lato",sans-serif;color:var(--ink)}
.abs{position:absolute}

/* header */
.site-header{left:0;top:0;width:668px;height:67px;background:var(--white);border-top:2px solid var(--ink)}
.social{left:474px;top:5px;display:flex;gap:4px}
.social span{width:13px;height:13px;border-radius:2px;background:var(--steel)}
.phone-tab{left:550px;top:0;width:96px;height:18px;background:var(--ink);color:var(--white);font-size:10px;display:flex;align-items:center;gap:5px;padding-left:12px;clip-path:polygon(0 0,100% 0,94% 100%,6% 100%)}
.brand{left:38px;top:16px;display:flex;align-items:center;gap:7px}
.brand-mark{width:14px;height:14px;background:var(--ink)}
.brand-name{font-family:"Russo One",sans-serif;font-size:12px;letter-spacing:.5px;color:var(--ink);line-height:1.15}
.main-nav{top:40px;left:360px;display:flex;gap:30px;font-family:"Russo One",sans-serif;font-size:9px;color:var(--ink)}
.main-nav a{color:inherit;text-decoration:none;position:relative}
.main-nav a.active{color:#555}
.main-nav a.active::before,.main-nav a.active::after{content:"";position:absolute;left:0;right:0;height:1px;background:#555}
.main-nav a.active::before{top:-4px}
.main-nav a.active::after{bottom:-4px}

/* hero */
.hero{left:0;top:67px;width:668px;height:278px;background:linear-gradient(100deg,#6d5a43 0%,#c9bfae 22%,#e6e3dd 45%,#d7d8d9 70%,#b9bcbe 100%)}
.hero-band{left:273px;top:232px;width:395px;height:58px;background:rgba(20,20,20,.72);color:var(--white);font-family:"Oswald",sans-serif;text-align:right;padding:8px 34px 0 0}
.hero-band .lead{font-size:19px;letter-spacing:-.2px;line-height:22px}
.hero-band .sub{font-size:14px;line-height:19px}

/* dividers */
.divider{left:194px;width:280px;height:14px}
.divider::before{content:"";position:absolute;left:0;right:0;top:7px;height:1px;background:var(--silver)}
.divider i{position:absolute;left:135px;top:2px;width:10px;height:10px;border-radius:50%;background:var(--ink);box-shadow:0 0 0 3px var(--mist)}
.divider.on-white i{box-shadow:0 0 0 3px var(--white)}
.divider.on-dark::before{background:#6a6a6a}
.divider.on-dark i{background:var(--white);box-shadow:0 0 0 3px var(--night)}

/* welcome */
.welcome{left:0;top:345px;width:668px;height:187px;background:var(--mist)}
.welcome h1{position:absolute;top:23px;width:100%;text-align:center;font-family:"Russo One",sans-serif;font-weight:400;font-size:16px;letter-spacing:.5px;color:#3a3a3a}
.welcome h1 b{font-weight:400;color:var(--ink)}
.welcome p{position:absolute;left:40px;top:80px;width:588px;text-align:center;font-size:8px;line-height:13.5px;color:#333}
.read-more{position:absolute;left:295px;top:139px;width:81px;height:20px;background:linear-gradient(#a9aaab,#8a8b8c);clip-path:polygon(0 0,93% 0,100% 50%,93% 100%,0 100%);color:var(--white);font-size:8px;display:flex;align-items:center;gap:6px;padding-left:4px}
.read-more i{width:14px;height:14px;border-radius:50%;background:var(--charcoal)}

/* gallery */
.gallery-head{left:0;top:532px;width:668px;height:83px;background:var(--white)}
.section-title{position:absolute;width:100%;text-align:center;font-family:"Russo One",sans-serif;font-weight:400;font-size:16px;letter-spacing:.6px}
.gallery-grid{left:0;top:615px;width:668px;height:266px;display:grid;grid-template-columns:repeat(5,1fr);grid-template-rows:repeat(2,1fr);gap:1px;background:var(--white)}
.tile{position:relative}
.t1{background:linear-gradient(90deg,#3a2a20,#7a6a58 60%,#c8b89c)}
.t2{background:linear-gradient(180deg,#c4ccd3,#5d6a78 60%,#39424e)}
.t3{background:linear-gradient(180deg,#4a5258,#6d767b)}
.t4{background:linear-gradient(180deg,#e8e8e8,#8a8e98 60%,#c9c9c9)}
.t5{background:linear-gradient(180deg,#c8c9c4,#7d7a72 70%,#5b5148)}
.t6{background:linear-gradient(180deg,#b7b3ad,#c78d5d 55%,#6a6a6a)}
.t7{background:linear-gradient(90deg,#5e6a6a,#c9d4d1 50%,#8f9598)}
.t8{background:linear-gradient(180deg,#e9ebeb,#b9bcbc 60%,#6f6a65)}
.t9{background:linear-gradient(180deg,#d9d6c6,#9aa58d 55%,#b85a2c 80%,#b8b4a6)}
.t10{background:linear-gradient(180deg,#d5d8d8,#4a4a48 60%,#7c6d60)}
.tile-hover{position:absolute;inset:0;background:rgba(40,40,40,.55);color:var(--white);text-align:center;padding-top:40px}
.tile-hover h3{font-size:14px;font-weight:700;margin-bottom:8px}
.tile-hover p{font-size:7px;line-height:11px;padding:0 14px}

/* contact */
.contact{left:0;top:881px;width:668px;height:287px;background:linear-gradient(135deg,#2b2c2e,#161718 55%,#2a2b2d)}
.contact .section-title{color:var(--white);top:20px}
.contact-form{position:absolute;left:34px;top:109px;width:180px}
.field{display:block;width:180px;height:23px;background:var(--white);border:none;font-family:"Lato",sans-serif;font-size:8px;color:#333;padding:0 8px;margin-bottom:4px;line-height:23px}
.field.message{height:43px;line-height:normal;padding-top:8px}
.submit{display:block;width:77px;height:26px;margin-top:4px;background:linear-gradient(#9b9c9d,#6f7071);color:var(--white);font-weight:700;font-size:11px;line-height:26px;text-align:center}
.map{position:absolute;left:272px;top:107px;width:135px;height:153px}
.contact-info{position:absolute;left:465px;top:121px;width:167px;color:var(--white);font-size:8px}
.info-row{display:flex;gap:7px;padding-bottom:12px}
.info-row + .info-row{border-top:1px solid #4a4a4a;padding-top:12px}
.info-row svg{flex:none;margin-top:1px}
.info-row strong{font-weight:700;display:block;margin-bottom:4px}
.info-row .addr{line-height:11px}
.site-footer{left:0;top:1168px;width:668px;height:32px;background:var(--footer);color:var(--white);font-size:7px;font-weight:700;text-align:center;line-height:32px}
</style>
</head>
<body>

<header class="site-header abs">
  <div class="social abs" aria-label="Social links"><span></span><span></span><span></span><span></span></div>
  <div class="phone-tab abs">
    <svg width="9" height="9" viewBox="0 0 24 24" fill="#fff"><path d="M6.6 10.8a15.1 15.1 0 0 0 6.6 6.6l2.2-2.2c.3-.3.7-.4 1-.2 1.1.4 2.3.6 3.6.6.6 0 1 .4 1 1V20c0 .6-.4 1-1 1A17 17 0 0 1 3 4c0-.6.4-1 1-1h3.5c.6 0 1 .4 1 1 0 1.3.2 2.5.6 3.6.1.3 0 .7-.2 1z"/></svg>
    07 3555 0142
  </div>
  <div class="brand abs">
    <span class="brand-mark"></span>
    <span class="brand-name">TALLOW BRIDGE</span>
  </div>
  <nav class="main-nav abs">
    <a class="active" href="#">HOME</a>
    <a href="#">ABOUT US</a>
    <a href="#">PORTFOLIO</a>
    <a href="#">CONTACT US</a>
  </nav>
</header>

<section class="hero abs" role="img" aria-label="Photo of a bright office fit out with glass partitions and timber doors">
</section>
<div class="hero-band abs">
  <div class="lead">WE SPECIALISE IN COMMERCIAL OFFICE FIT OUTS</div>
  <div class="sub">(PARTITIONS/GLASS/DOORS)</div>
</div>

<section class="welcome abs">
  <h1>WELCOME TO <b>TALLOW BRIDGE</b></h1>
  <div class="divider abs" style="top:56px"><i></i></div>
  <p>Lorem ipsum dolor sit amet, consectetuer adipiscing elit, sed diam nonummy nibh euismod tincidunt ut laoreet dolore magna aliquam erat volutpat. Ut wisi enim ad minim veniam, quis nostrud exerci tation ullamcorper suscipit lobortis nisl ut aliquip ex ea commodo consequat. Duis autem vel eum iriure dolor in hendrerit in vulputate velit esse molestie consequat, vel illum dolore eu feugiat nulla facilisis at vero eros et accumsan et</p>
  <div class="read-more"><i></i>READ MORE</div>
</section>

<section class="gallery-head abs">
  <h2 class="section-title" style="top:25px">PROJECT GALLERY</h2>
  <div class="divider on-white abs" style="top:52px"><i></i></div>
</section>
<div class="gallery-grid abs">
  <div class="tile t1" role="img" aria-label="Photo of a dark timber door with glass panels"></div>
  <div class="tile t2" role="img" aria-label="Photo of office workstations with blue partitions"></div>
  <div class="tile t3" role="img" aria-label="Photo of a glass-walled meeting room">
    <div class="tile-hover"><h3>High Wall</h3><p>Sed ut perspiciatis unde om erere nis iste natus error sit voluptatem accusanti</p></div>
  </div>
  <div class="tile t4" role="img" aria-label="Photo of modular office partition screens"></div>
  <div class="tile t5" role="img" aria-label="Photo of black-framed glass office partitions"></div>
  <div class="tile t6" role="img" aria-label="Photo of a timber reception counter"></div>
  <div class="tile t7" role="img" aria-label="Photo of frosted glass sliding doors"></div>
  <div class="tile t8" role="img" aria-label="Photo of glass partitions with frosted bands"></div>
  <div class="tile t9" role="img" aria-label="Photo of a curved glass meeting room with a plant"></div>
  <div class="tile t10" role="img" aria-label="Photo of a black grid glass office wall"></div>
</div>

<section class="contact abs">
  <h2 class="section-title">CONTACT US</h2>
  <div class="divider on-dark abs" style="top:50px"><i></i></div>

  <form class="contact-form">
    <div class="field">Name</div>
    <div class="field">Email</div>
    <div class="field">Phone</div>
    <div class="field message">Message</div>
    <div class="submit">Submit</div>
  </form>

  <svg class="map" viewBox="0 0 135 153" role="img" aria-label="Street map showing the office location">
    <defs><linearGradient id="mapTone" x1="0" y1="0" x2="1" y2="1"><stop offset="0" stop-color="#e8e4d6"/><stop offset=".5" stop-color="#c9d6c2"/><stop offset="1" stop-color="#b9cfe0"/></linearGradient></defs>
    <polygon points="67.5,2 132,39 132,114 67.5,151 3,114 3,39" fill="url(#mapTone)" stroke="#d9d9d9" stroke-width="3"/>
  </svg>

  <div class="contact-info">
    <div class="info-row">
      <svg width="8" height="11" viewBox="0 0 16 22" fill="#fff"><path d="M8 0a8 8 0 0 0-8 8c0 6 8 14 8 14s8-8 8-14a8 8 0 0 0-8-8zm0 11a3 3 0 1 1 0-6 3 3 0 0 1 0 6z"/></svg>
      <div><strong>TALLOW BRIDGE (QLD) PTY LTD.</strong><div class="addr">123, Lorem ipsum dolo sit amet<br>&nbsp;AB &nbsp;nonumm 1213454</div></div>
    </div>
    <div class="info-row">
      <svg width="9" height="9" viewBox="0 0 24 24" fill="#fff"><path d="M6.6 10.8a15.1 15.1 0 0 0 6.6 6.6l2.2-2.2c.3-.3.7-.4 1-.2 1.1.4 2.3.6 3.6.6.6 0 1 .4 1 1V20c0 .6-.4 1-1 1A17 17 0 0 1 3 4c0-.6.4-1 1-1h3.5c.6 0 1 .4 1 1 0 1.3.2 2.5.6 3.6.1.3 0 .7-.2 1z"/></svg>
      <div>07 3555 0142</div>
    </div>
    <div class="info-row">
      <svg width="10" height="8" viewBox="0 0 20 16" fill="#fff"><path d="M0 0h20v2l-10 6L0 2z"/><path d="M0 4l10 6 10-6v12H0z"/></svg>
      <div>info@tallowbridge.com</div>
    </div>
  </div>
</section>

<footer class="site-footer abs">COPYRIGHT © 2016 TALLOW BRIDGE (QLD) PTY LTD. ALL RIGHTS RESERVED</footer>

</body>
</html>
```